Copper Finch Agency Website - Wordpress Web UPDATED BRIEF

FINAL LOGO UPLOADED - please look to this as reference for how we would like the site to look and feel.

We are a digital marketing agency - looking to have a new website built. We are looking for a simple one page feel of site that will allow us to grow it later. (Feel free to take some liberties with that if your imagination veers off) Must be very, playful, bold, sleek and easily integrate video. Wordpress only.

Overview:

Copper Finch is a creative constellation. We are built on what's great about the shared economy. With access to thousands of content creators, designers, technicians, writers, strategists and other creatives around the world, we are built differently than a traditional “brick and mortar” Marketing Agency. We provide the traditional services our clients have come to expect, without the “5X factor” of covering the overhead common in the old agency model. We believe even better work can be created in collaboration with our clients and by passing those savings back to them for their use. Our clients pay for our art, our work and our passion –not our furniture.

"Copper Finch, Let's Start Something"

Target Market(s)

companies looking for creative agency help, video production, creative consulting and coaching

Industry/Entity Type

Digital Marketing

Coding

Coded - Design and coding required

Number of Pages Required

1 page

Font styles to use
Sans Serif

Colors
3277b5
33a6d7
ec1f27

Requirements
Must have
• Wordpress design is a must. Looking for a one sheet homepage - with sections that are all on the main front page. We will have videos to embed, and should be able to have client logos and easy access to show a variety of our creative work.
• Please look to the logo for how we would like the site to feel.
• Please think "icon process flow" instead of blocks of text (which we used to have). Use the text to explain what the process flow should represent - don't actually copy paste the text but show it visually in icons.
Nice to have
• innovation around how we show video content. solid colors complementary to our palette and aesthetic.
Should not have
• Standard HTML coding

```html
<!DOCTYPE html>
<html lang="en">
<head>
<meta charset="utf-8">
<title>Copper Finch Agency</title>
<link href="https://fonts.googleapis.com/css2?family=Poppins:wght@300;400;500;600;700&family=Oswald:wght@400;500&display=swap" rel="stylesheet">
<style>
:root{
  --blue:#3277b5;
  --sky:#33a6d7;
  --red:#ec1f27;
  --ink:#222630;
  --text:#6b6f78;
  --muted:#9a9ea6;
  --line:#e3e6ea;
  --pale:#eef6fb;
  --foot:#2c2d33;
  --white:#fff;
}
*{box-sizing:border-box;margin:0;padding:0}
html,body{width:1200px;height:4091px;overflow:hidden}
body{font-family:"Poppins",sans-serif;color:var(--ink);background:var(--white);position:relative}
.abs{position:absolute}
a{text-decoration:none;color:inherit}

/* header */
.site-header{position:absolute;top:0;left:0;width:1200px;height:98px;background:var(--white);z-index:3}
.brand{position:absolute;left:74px;top:22px;display:flex;align-items:center;gap:10px;font-weight:700;font-size:20px;color:var(--blue)}
.brand-dot{width:40px;height:40px;border-radius:50%;background:var(--blue)}
.main-nav{position:absolute;left:410px;top:38px;display:flex;gap:0;font-size:13px;color:var(--text)}
.main-nav a{width:94px}
.main-nav a.active{color:var(--blue)}
.nav-phone{position:absolute;left:888px;top:38px;font-size:13px;color:var(--ink);display:flex;gap:6px;align-items:center}
.btn{display:inline-flex;align-items:center;justify-content:center;border-radius:30px;font-size:12px;font-weight:500;color:var(--white)}
.btn-blue{background:linear-gradient(90deg,var(--blue),var(--sky))}
.btn-red{background:var(--red)}
.hire{position:absolute;left:1023px;top:26px;width:96px;height:40px}

/* hero */
.hero{position:absolute;top:98px;left:0;width:1200px;height:543px;background:linear-gradient(100deg,#2b3440 0%,#55616f 40%,#8b8b86 60%,#3b4a5a 100%)}
.hero-title{position:absolute;left:162px;top:150px;font-size:38px;line-height:48px;font-weight:600;color:var(--white);width:520px}
.hero-sub{position:absolute;left:162px;top:258px;font-size:15px;line-height:24px;color:#eef;width:360px}
.hero-btn{position:absolute;left:162px;top:332px;width:178px;height:40px}
.lead-card{position:absolute;left:769px;top:66px;width:270px;height:403px;background:var(--white);text-align:center;padding-top:22px}
.lead-card .small{font-size:13px;font-weight:600}
.lead-card .tag{font-family:"Oswald",sans-serif;font-size:18px;color:var(--red);margin-top:4px}
.field{border:1px solid var(--line);border-radius:20px;height:30px;font-size:11px;color:var(--muted);text-align:left;padding:7px 14px;margin:0 auto 11px;width:226px}
.lead-card .fields{margin-top:16px}
.field.area{height:72px;border-radius:14px}
.lead-card .send{width:96px;height:38px;margin-top:10px}

/* process */
.process{position:absolute;top:641px;left:0;width:1200px;height:431px}
.step{position:absolute;top:63px;width:273px;height:305px;text-align:center;padding-top:56px}
.step.boxed{border:2px solid #7cc3e6;border-radius:4px}
.step h3{font-size:18px;font-weight:600;margin-top:16px}
.step p{font-size:14px;line-height:22px;color:var(--text);width:200px;margin:10px auto 0}
.more{font-size:11px;color:var(--sky);display:block;margin-top:14px}

/* band */
.values{position:absolute;top:1072px;left:0;width:1200px;height:237px;background:linear-gradient(90deg,var(--blue),#3a86c2);color:var(--white);text-align:center}
.values h2{font-size:30px;font-weight:300;margin-top:54px}
.values h2 b{font-weight:600}
.values p{font-size:12px;margin-top:4px;opacity:.85}
.pill{position:absolute;top:147px;width:274px;height:56px;background:var(--white);border-radius:30px;display:flex;align-items:center;font-family:"Oswald",sans-serif;font-size:19px;color:var(--blue)}
.pill .ico{width:46px;height:46px;border-radius:50%;background:var(--blue);margin:0 20px 0 5px;display:flex;align-items:center;justify-content:center}

/* about */
.about{position:absolute;top:1309px;left:0;width:1200px;height:524px}
.about h2{position:absolute;left:82px;top:80px;font-size:27px;font-weight:600}
.about .copy{position:absolute;left:82px;top:136px;width:440px;font-size:14px;line-height:22px;color:var(--text)}
.about .copy p+p{font-size:11.5px;line-height:19px;margin-top:16px}
.about .btn{position:absolute;left:82px;top:400px;width:110px;height:40px}
.about-photo{position:absolute;left:600px;top:6px;width:600px;height:518px;background:linear-gradient(135deg,#5e6a72,#8f969a 50%,#3d4a55)}

/* services */
.services{position:absolute;top:1833px;left:0;width:1200px;height:512px}
.svc{position:absolute;top:65px;width:200px;height:290px;text-align:center;padding-top:46px}
.svc.boxed{border:2px solid #7cc3e6;border-radius:4px}
.svc h3{font-size:14px;font-weight:600;margin-top:12px}
.svc p{font-size:11.5px;line-height:19px;color:var(--text);width:164px;margin:8px auto 0}
.arrow{position:absolute;top:205px}
.view-all{position:absolute;left:545px;top:398px;width:110px;height:38px}

/* work */
.work{position:absolute;top:2345px;left:0;width:1200px;height:587px;background:var(--pale);overflow:hidden}
.work h2{position:absolute;top:82px;width:100%;text-align:center;font-size:27px;font-weight:600}
.slide{position:absolute;top:145px;height:360px}
.slide.main{left:161px;width:878px;background:linear-gradient(135deg,#2aa1cf,#1c8cb5 55%,#5cc9ec)}
.slide.left{left:0;width:126px;background:linear-gradient(180deg,#f8c12e,#f2a72c)}
.slide.right{left:1072px;width:128px;background:#1d2533}
.slide-cap{position:absolute;left:40px;bottom:46px;color:var(--white)}
.slide-cap b{font-size:20px;font-weight:600;display:block}
.slide-cap span{font-size:12px}
.dots{position:absolute;top:537px;left:0;width:100%;display:flex;justify-content:center;gap:6px}
.dots i{width:9px;height:9px;border-radius:50%;border:1px solid var(--sky)}
.dots i:first-child{background:var(--sky)}

/* testimonials */
.voices{position:absolute;top:2932px;left:0;width:1200px;height:450px}
.voices h2{position:absolute;top:68px;width:100%;text-align:center;font-size:27px;font-weight:600}
.avatar{position:absolute;top:150px;width:110px;height:110px;border-radius:50%;background:linear-gradient(135deg,#c9d8e4,#e9eef2)}
.quote{position:absolute;top:150px;width:290px;font-size:13.5px;line-height:24px;color:var(--text)}
.who{position:absolute;top:330px;font-size:13px;color:var(--sky);font-weight:500}
.who small{display:block;color:var(--ink);font-size:11px;font-weight:400}

/* clients */
.clients-label{position:absolute;top:3388px;left:82px;width:1036px;display:flex;align-items:center;gap:20px;font-size:15px;font-weight:500}
.clients-label::before,.clients-label::after{content:"";flex:1;height:1px;background:var(--line)}
.logo-row{position:absolute;top:3478px;left:150px;width:900px;display:flex;justify-content:space-between;font-size:24px;font-weight:600;color:#9aa0a8}
.logo-row span{width:150px;text-align:center}

/* contact */
.contact{position:absolute;top:3600px;left:0;width:1200px;height:423px;background:linear-gradient(180deg,#fff 0%,#fff 70%,#d7dde4 100%)}
.contact h2{position:absolute;top:36px;width:100%;text-align:center;font-size:27px;line-height:38px;font-weight:600}
.cfield{position:absolute;height:42px;border:1px solid var(--line);border-radius:22px;font-size:11px;color:var(--muted);padding:13px 20px;background:var(--white)}
.cfield.area{border-radius:16px;height:92px}
.contact .send{position:absolute;left:554px;top:322px;width:96px;height:40px}

/* footer */
.site-footer{position:absolute;top:4023px;left:0;width:1200px;height:68px;background:var(--foot);color:#b8bbc2;font-size:12px}
.site-footer .info{position:absolute;left:80px;top:26px;display:flex;gap:60px}
.soc{position:absolute;top:0;width:78px;height:68px;display:flex;align-items:center;justify-content:center}
</style>
</head>
<body>

<header class="site-header">
  <a class="brand" href="#"><span class="brand-dot"></span>Copper Finch</a>
  <nav class="main-nav">
    <a class="active" href="#">Home</a><a href="#">About</a><a href="#">Service</a><a href="#">Work</a><a href="#">Client</a><a href="#">Reviews</a>
  </nav>
  <div class="nav-phone">
    <svg width="12" height="12" viewBox="0 0 24 24"><path d="M6 2l4 4-2 3a12 12 0 0 0 7 7l3-2 4 4-3 4C10 22 2 14 2 5z" fill="#222630"/></svg>555.014.2290
  </div>
  <a class="btn btn-blue hire" href="#">Hire Us!</a>
</header>

<section class="hero">
  <div class="abs" role="img" aria-label="Photo of a smiling team member working at a table with colleagues" style="inset:0"></div>
  <h1 class="hero-title">Leading best digital marketing agency.</h1>
  <p class="hero-sub">looking to have a new website built. We are looking for a simple one page</p>
  <a class="btn btn-blue hero-btn" href="#">Contact Us Today!</a>
  <form class="lead-card">
    <div class="small">Copper Finch</div>
    <div class="tag">LET'S START SOMETHING</div>
    <div class="fields">
      <div class="field">Your Name</div>
      <div class="field">Email</div>
      <div class="field">Phone</div>
      <div class="field">Project Type</div>
      <div class="field area">Description</div>
    </div>
    <span class="btn btn-red send">Send</span>
  </form>
</section>

<section class="process">
  <div class="step boxed" style="left:158px">
    <svg width="54" height="54" viewBox="0 0 54 54" fill="none" stroke="#3277b5" stroke-width="2"><rect x="12" y="8" width="26" height="34" rx="2"/><circle cx="33" cy="34" r="9" stroke="#33a6d7"/><path d="M40 41l8 8" stroke="#ec1f27"/><path d="M17 16h14M17 22h10"/></svg>
    <h3>Discovery.</h3><p>We are passionate about creating with you, not just for you.</p><a class="more" href="#">Learn More →</a>
  </div>
  <div class="step" style="left:464px">
    <svg width="54" height="54" viewBox="0 0 54 54" fill="none" stroke="#3277b5" stroke-width="2"><path d="M16 46h24M19 40h18l-3-12c6-4 4-14-4-16l-8 4 4 4-6 8z"/><circle cx="30" cy="18" r="1.5" fill="#ec1f27" stroke="none"/></svg>
    <h3>Strategy.</h3><p>Content is only as good as your plan to deliver it.</p><a class="more" href="#">Learn More →</a>
  </div>
  <div class="step" style="left:769px">
    <svg width="54" height="54" viewBox="0 0 54 54" fill="none" stroke="#3277b5" stroke-width="2"><path d="M27 12a11 11 0 0 0-6 20v6h12v-6a11 11 0 0 0-6-20zM22 43h10"/><path d="M27 3v4M10 10l3 3M44 10l-3 3M5 24h4M45 24h4" stroke="#ec1f27"/></svg>
    <h3>Creative.</h3><p>We are ready for our close up! Are you?</p><a class="more" href="#">Learn More →</a>
  </div>
</section>

<section class="values">
  <h2>Better <b>Service</b> · Better <b>Experience</b> · A Better <b>Agency</b></h2>
  <p>Providing the best customer service in the Industry. Professionals of the Industry. Credible and reliable.</p>
  <div class="pill" style="left:158px"><span class="ico"><svg width="18" height="18" viewBox="0 0 24 24"><circle cx="12" cy="12" r="6" fill="none" stroke="#fff" stroke-width="4" stroke-dasharray="3 2"/></svg></span>CUSTOMER SERVICE</div>
  <div class="pill" style="left:464px"><span class="ico"><svg width="18" height="18" viewBox="0 0 24 24" fill="#fff"><circle cx="12" cy="8" r="4"/><path d="M4 21a8 8 0 0 1 16 0z"/></svg></span>PROFESSIONALISM</div>
  <div class="pill" style="left:766px"><span class="ico"><svg width="18" height="18" viewBox="0 0 24 24" fill="#fff"><path d="M3 10h4v11H3zM9 21h9l3-9h-7l1-6-2-2-4 7z"/></svg></span>CREDIBLE &amp; RELIABLE</div>
</section>

<section class="about">
  <h2>About Copper Finch</h2>
  <div class="copy">
    <p>Copper Finch is a creative constellation. We are built on what's great about the shared economy. With access to thousands of content creators, designers, technicians, writers, strategists and other creatives around the world.</p>
    <p>we are built differently than a traditional “brick and mortar” Marketing Agency. We provide the traditional services our clients have come to expect, without the “5X factor” of covering the overhead common in the old agency model. We believe even better work can be created in collaboration with our clients and by passing those savings back to them for their use. Our clients pay for our art, our work and our passion –not our furniture.</p>
  </div>
  <a class="btn btn-blue" href="#">About Us</a>
  <div class="about-photo" role="img" aria-label="Overhead photo of a team working on laptops at a shared table"></div>
</section>

<section class="services">
  <svg class="arrow" style="left:110px" width="14" height="14" viewBox="0 0 14 14"><path d="M9 2L4 7l5 5" fill="none" stroke="#b7bcc3" stroke-width="1.5"/></svg>
  <svg class="arrow" style="left:1074px" width="14" height="14" viewBox="0 0 14 14"><path d="M5 2l5 5-5 5" fill="none" stroke="#b7bcc3" stroke-width="1.5"/></svg>
  <div class="svc" style="left:158px">
    <svg width="44" height="44" viewBox="0 0 44 44" fill="none" stroke="#3277b5" stroke-width="2"><rect x="6" y="8" width="32" height="22"/><path d="M12 24l6-6 5 4 8-8" stroke="#ec1f27"/><path d="M16 38h12M22 30v8"/></svg>
    <h3>Management</h3><p>Lorem ipsum dolor amet, consectetur adipiscing elit, sed do eiusmod tempor incididunt ut ...</p><a class="more" href="#">Learn More →</a>
  </div>
  <div class="svc boxed" style="left:387px">
    <svg width="44" height="44" viewBox="0 0 44 44" fill="none" stroke="#3277b5" stroke-width="2"><rect x="5" y="8" width="34" height="28" rx="2"/><path d="M5 15h34"/><circle cx="18" cy="26" r="5" stroke="#ec1f27"/><path d="M27 23h7M27 29h7"/></svg>
    <h3>Content</h3><p>Lorem ipsum dolor amet, consectetur adipiscing elit, sed do eiusmod tempor incididunt ut ...</p><a class="more" href="#">Learn More →</a>
  </div>
  <div class="svc" style="left:614px">
    <svg width="44" height="44" viewBox="0 0 44 44" fill="none" stroke="#3277b5" stroke-width="2"><circle cx="22" cy="22" r="12" stroke-dasharray="5 3"/><circle cx="22" cy="22" r="5" stroke="#ec1f27"/></svg>
    <h3>Production</h3><p>Lorem ipsum dolor amet, consectetur adipiscing elit, sed do eiusmod tempor incididunt ut ...</p><a class="more" href="#">Learn More →</a>
  </div>
  <div class="svc" style="left:840px">
    <svg width="44" height="44" viewBox="0 0 44 44" fill="none" stroke="#3277b5" stroke-width="2"><path d="M10 34l10-4 12-16-6-4-12 16z"/><path d="M28 6l8 6" stroke="#ec1f27"/><circle cx="12" cy="12" r="4"/></svg>
    <h3>Paid Media</h3><p>Lorem ipsum dolor amet, consectetur adipiscing elit, sed do eiusmod tempor incididunt ut ...</p><a class="more" href="#">Learn More →</a>
  </div>
  <a class="btn btn-blue view-all" href="#">View All</a>
</section>

<section class="work">
  <h2>Explore Our Work</h2>
  <div class="slide left" role="img" aria-label="Project preview with yellow and blue shapes"></div>
  <div class="slide main" role="img" aria-label="Project preview of a data management dashboard on a screen">
    <div class="slide-cap"><b>Big Data Management System Frontend</b><span>Web Application</span></div>
  </div>
  <div class="slide right" role="img" aria-label="Project preview on a dark screen"></div>
  <div class="dots"><i></i><i></i><i></i><i></i><i></i><i></i><i></i><i></i></div>
</section>

<section class="voices">
  <h2>What Our Clients Say</h2>
  <svg class="abs" style="left:110px;top:215px" width="14" height="14" viewBox="0 0 14 14"><path d="M9 2L4 7l5 5" fill="none" stroke="#b7bcc3" stroke-width="1.5"/></svg>
  <svg class="abs" style="left:1074px;top:215px" width="14" height="14" viewBox="0 0 14 14"><path d="M5 2l5 5-5 5" fill="none" stroke="#b7bcc3" stroke-width="1.5"/></svg>
  <div class="avatar" style="left:169px" role="img" aria-label="Portrait of Marla Quinn"></div>
  <p class="quote" style="left:314px">There are many variations of passages of Lorem Ipsum available, but the majority have suffered alteration in some form, by injected humour, or randomised words which don't look even slightly believable.</p>
  <div class="who" style="left:314px">Marla Quinn,<small>Lantern Stage</small></div>
  <div class="avatar" style="left:636px" role="img" aria-label="Portrait of Theo Brandt"></div>
  <p class="quote" style="left:783px">There are many variations of passages of Lorem Ipsum available, but the majority have suffered alteration in some form, by injected humour, or randomised words which don't look even slightly believable.</p>
  <div class="who" style="left:783px">Theo Brandt<small>Collective</small></div>
</section>

<div class="clients-label">Clients</div>
<div class="logo-row"><span>Firmline</span><span>Plainco</span><span>Tamaro</span><span>Plainco</span><span>Firmline</span></div>

<section class="contact">
  <div class="abs" role="img" aria-label="Soft misty mountain landscape" style="left:0;bottom:0;width:1200px;height:130px;background:linear-gradient(180deg,rgba(255,255,255,0),#c8d1da)"></div>
  <h2>Copper Finch, Let's Start<br>Something!</h2>
  <div class="cfield" style="left:240px;top:150px;width:354px">Enter your Name*</div>
  <div class="cfield" style="left:611px;top:150px;width:349px">Project Type*</div>
  <div class="cfield" style="left:240px;top:206px;width:354px">E-mail*</div>
  <div class="cfield area" style="left:611px;top:188px;width:349px">Message</div>
  <div class="cfield" style="left:240px;top:262px;width:354px">Phone</div>
  <span class="btn btn-red send">Send</span>
</section>

<footer class="site-footer">
  <div class="info"><span>© 2019 COPPER FINCH</span><span>PH: 555.014.2290</span><span>E: HELLO@COPPERFINCH.CO</span></div>
  <div class="soc" style="left:966px;background:#3b3c43"><svg width="16" height="20" viewBox="0 0 16 20"><path d="M8 0a7 7 0 0 0-7 7c0 5 7 13 7 13s7-8 7-13a7 7 0 0 0-7-7z" fill="#b8bbc2"/><circle cx="8" cy="7" r="2.5" fill="#3b3c43"/></svg></div>
  <div class="soc" style="left:1044px;background:#3b5a9a"><span style="width:10px;height:10px;border-radius:50%;background:#fff"></span></div>
  <div class="soc" style="left:1122px;background:#2c79b8"><span style="width:10px;height:10px;background:#fff"></span></div>
</footer>

</body>
</html>
```